Zarvenok Play Home Page and Logo

We are looking to update the Zarvenok Logo and Branding as well as the Home Page (https://www.zarvenok-play.example). The Home Page is PRIORITY number 1. We are looking for something that is eye catching and satisfies a very eclectic community from all nations across the world yet want to modernize the game instead of being stuck in the 90's.

```html
<!DOCTYPE html>
<html lang="en">
<head>
<meta charset="utf-8">
<title>Zarvenok Web design UI</title>
<link rel="stylesheet" href="https://fonts.googleapis.com/css2?family=Poppins:wght@400;500&family=Kalam:wght@400;700&display=swap">
<style>
  :root {
    --page-bg: #242424;
    --screen-bg: #1e1e1e;
    --header-bg: #161616;
    --nav-bg: #3b3b3b;
    --field-bg: #4a4a4a;
    --accent: #d32222;
    --mobile-bar: #b33a3a;
    --mobile-field: #c86262;
    --text-light: #f2f2f2;
    --text-body: #d9d9d9;
    --band: rgba(255,255,255,0.22);
  }
  * { box-sizing: border-box; margin: 0; padding: 0; }
  html, body { width: 1200px; height: 963px; overflow: hidden; }
  body {
    background: var(--page-bg);
    font-family: "Poppins", sans-serif;
    color: var(--text-light);
    position: relative;
  }
  .showcase-title {
    position: absolute; top: 34px; left: 0; width: 100%;
    text-align: center; font-size: 40px; font-weight: 400;
  }
  .showcase-subtitle {
    position: absolute; top: 100px; left: 0; width: 100%;
    text-align: center; font-size: 23px; font-weight: 400; color: var(--text-body);
  }

  /* Desktop screen */
  .desktop {
    position: absolute; left: 215px; top: 221px; width: 798px; height: 502px;
    background: var(--screen-bg); overflow: hidden;
  }
  .desktop-header { position: absolute; left: 0; top: 0; width: 100%; height: 103px; background: var(--header-bg); }
  .brand {
    position: absolute; left: 21px; top: 20px; width: 118px; height: 67px;
    display: flex; align-items: center; gap: 8px;
    font-size: 17px; font-weight: 500; color: var(--text-light);
  }
  .brand-mark { width: 14px; height: 14px; background: var(--accent); flex: none; }
  .search-field {
    position: absolute; left: 179px; top: 36px; width: 298px; height: 33px;
    background: var(--field-bg); border-radius: 3px;
    padding-left: 25px; line-height: 33px; font-size: 16px; color: #aaa;
  }
  .btn {
    position: absolute; top: 36px; width: 100px; height: 33px; border-radius: 3px;
    text-align: center; line-height: 31px; font-size: 14px; color: var(--text-light);
  }
  .btn-login { left: 549px; border: 1.5px solid var(--text-light); }
  .btn-signup { left: 669px; background: var(--accent); line-height: 33px; }
  .main-nav {
    position: absolute; left: 0; top: 103px; width: 100%; height: 51px;
    background: var(--nav-bg);
  }
  .nav-item { position: absolute; top: 0; height: 51px; line-height: 51px; font-size: 17px; color: var(--text-light); }
  .nav-item.active { background: var(--accent); padding: 0 10px; }
  .nav-search { position: absolute; left: 670px; top: 14px; }
  .hero {
    position: absolute; left: 0; top: 154px; width: 100%; height: 348px;
    background: radial-gradient(ellipse at 62% 30%, #c9d4a6 0%, #7f8d6c 25%, #46524a 55%, #26302f 100%);
  }
  .age-band {
    position: absolute; left: 0; top: 131px; width: 229px; height: 50px;
    background: var(--band);
    padding-left: 26px; line-height: 50px;
    font-family: "Kalam", cursive; font-weight: 700; font-size: 20px; letter-spacing: 1px;
  }
  .hero-title {
    position: absolute; left: 26px; top: 240px; width: 560px;
    font-family: "Kalam", cursive; font-size: 50px; line-height: 64px; font-weight: 400;
  }

  /* Mobile screen */
  .mobile {
    position: absolute; left: 890px; top: 357px; width: 267px; height: 576px;
    background: var(--screen-bg); overflow: hidden; border-radius: 28px 28px 0 0;
  }
  .mobile-bar { position: absolute; left: 0; top: 0; width: 100%; height: 56px; background: var(--mobile-bar); }
  .status-time { position: absolute; left: 22px; top: 5px; font-size: 11px; font-weight: 500; }
  .status-icons { position: absolute; right: 14px; top: 8px; }
  .menu-icon { position: absolute; left: 12px; top: 33px; }
  .mobile-search {
    position: absolute; left: 57px; top: 31px; width: 200px; height: 21px;
    background: var(--mobile-field); border-radius: 3px;
    font-size: 9px; line-height: 21px; padding-left: 14px; color: #f0dada;
  }
  .mobile-hero {
    position: absolute; left: 0; top: 56px; width: 100%; height: 151px;
    background: radial-gradient(ellipse at 50% 25%, #c5d0a4 0%, #7c8a6a 30%, #414c46 65%, #262d2c 100%);
  }
  .mobile-age {
    position: absolute; left: 0; top: 46px; width: 66px; height: 16px; background: var(--band);
    font-family: "Kalam", cursive; font-weight: 700; font-size: 7px; line-height: 16px; padding-left: 6px;
  }
  .mobile-hero-title {
    position: absolute; left: 7px; top: 84px; font-family: "Kalam", cursive; font-size: 16px; line-height: 21px;
  }
  .mobile-hero-tag { position: absolute; left: 7px; top: 127px; font-size: 6px; line-height: 8px; color: var(--text-body); }
  .feature { position: absolute; left: 12px; width: 236px; }
  .feature-title { font-size: 21px; font-weight: 400; line-height: 30px; }
  .feature-rule { width: 86px; height: 2.5px; background: var(--accent); margin: 2px 0 12px; }
  .feature-text { font-size: 11.5px; line-height: 18px; color: var(--text-body); }
</style>
</head>
<body>
  <h1 class="showcase-title">Zarvenok Web design UI</h1>
  <p class="showcase-subtitle">Check the other pages for the complete Designs.</p>

  <section class="desktop">
    <header class="desktop-header">
      <div class="brand"><span class="brand-mark"></span>Zarvenok</div>
      <div class="search-field">Search...</div>
      <div class="btn btn-login">Login</div>
      <div class="btn btn-signup">Sign Up</div>
    </header>
    <nav class="main-nav">
      <span class="nav-item active" style="left:45px">Home</span>
      <span class="nav-item" style="left:120px">Forum</span>
      <span class="nav-item" style="left:191px">Rules</span>
      <span class="nav-item" style="left:254px">Guide</span>
      <span class="nav-item" style="left:331px">Wiki</span>
      <span class="nav-item" style="left:394px">Blog</span>
      <svg class="nav-search" width="22" height="22" viewBox="0 0 22 22"><circle cx="9" cy="9" r="7" fill="none" stroke="#f2f2f2" stroke-width="2"/><line x1="14" y1="14" x2="20" y2="20" stroke="#f2f2f2" stroke-width="2"/></svg>
    </nav>
    <div class="hero" role="img" aria-label="Hero artwork: giant stone mask with glowing eye among green-grey clouds">
      <div class="age-band">AGE 42</div>
      <h2 class="hero-title">Zarvenok Ascent: Age of Ember</h2>
    </div>
  </section>

  <section class="mobile">
    <div class="mobile-bar">
      <span class="status-time">19:02</span>
      <svg class="status-icons" width="34" height="9" viewBox="0 0 34 9"><rect x="0" y="5" width="2" height="4" fill="#fff"/><rect x="3" y="3" width="2" height="6" fill="#fff"/><rect x="6" y="1" width="2" height="8" fill="#fff"/><rect x="20" y="1" width="12" height="7" rx="1.5" fill="none" stroke="#fff"/><rect x="21.5" y="2.5" width="9" height="4" fill="#fff"/></svg>
      <svg class="menu-icon" width="26" height="16" viewBox="0 0 26 16"><rect y="0" width="26" height="3" fill="#1e1e1e"/><rect y="6.5" width="26" height="3" fill="#1e1e1e"/><rect y="13" width="26" height="3" fill="#1e1e1e"/></svg>
      <div class="mobile-search">Search...</div>
    </div>
    <div class="mobile-hero" role="img" aria-label="Hero artwork: stone mask in clouds with a lone figure on a cliff">
      <div class="mobile-age">AGE 42</div>
      <div class="mobile-hero-title">Zarvenok Ascent: Age of<br>Ember</div>
      <div class="mobile-hero-tag">Rise, plan and fight</div>
    </div>
    <article class="feature" style="top:214px">
      <h3 class="feature-title">Strategy</h3>
      <div class="feature-rule"></div>
      <p class="feature-text">Build, explore and research to increase your power. Then use armies, thieves and powerful magic to combat your opponents and bring them to their knees.</p>
    </article>
    <article class="feature" style="top:369px">
      <h3 class="feature-title">Teamwork</h3>
      <div class="feature-rule"></div>
      <p class="feature-text">In Zarvenok a good team is stronger than the sum of its parts. Complement the skills of your team mates to maximize your kingdom's glory.</p>
    </article>
    <article class="feature" style="top:505px">
      <h3 class="feature-title">Free &amp; Compatabale</h3>
      <div class="feature-rule"></div>
      <p class="feature-text">Zarvenok is free to play, no downloads</p>
    </article>
  </section>
</body>
</html>
```